Need help in designing new business card utilizing our new logo.

BuildMarq Solutions works with Construction Business Owners, Managers & IT Professionals to strengthen software usage and increase user productivity.

Our Construction Accounting and Mobile Field Management Software Clients engage with us in the following areas:

New Software Implementations
Software Re-Implementations
Redesigning Software Usage at the User Level
Project Coordination & Management
Continued Software Support

Old tag line:
Weighing Options - Implementing Solutions

www.buildmarq-solutions.example

Stride 4 is a product, but not needed for a new business card.

```html
<!DOCTYPE html>
<html lang="en">
<head>
<meta charset="utf-8">
<title>BuildMarq Solutions – Business Card</title>
<link rel="stylesheet" href="https://fonts.googleapis.com/css2?family=Roboto:wght@400;500;700&display=swap">
<style>
  :root {
    --brand-blue: #3440c2;
    --brand-blue-deep: #2a35a8;
    --card-white: #f7f7f7;
    --strip-grey: #e2e2e4;
    --text-grey: #9a9aa0;
    --backdrop: #ecebe8;
    --ink-white: #ffffff;
  }
  * { box-sizing: border-box; margin: 0; padding: 0; }
  html, body {
    width: 1200px; height: 780px; overflow: hidden;
    background: var(--backdrop);
    font-family: "Roboto", Arial, sans-serif;
  }
  .stage {
    width: 1200px; height: 780px;
    display: flex; align-items: center; justify-content: center; gap: 50px;
  }
  .card {
    position: relative;
    width: 540px; height: 309px;
    overflow: hidden;
    box-shadow: 0 6px 18px rgba(0,0,0,.18);
  }

  /* Front */
  .card-front { background: var(--card-white); }
  .front-brand {
    position: absolute; left: 36px; top: 58px;
    display: flex; align-items: center; gap: 16px;
  }
  .brand-square { width: 44px; height: 44px; background: var(--brand-blue); }
  .brand-divider { width: 2px; height: 62px; background: var(--brand-blue); }
  .brand-name {
    font-weight: 700; color: var(--brand-blue);
    font-size: 30px; line-height: 1; letter-spacing: .5px;
  }
  .brand-sub {
    display: block; margin-top: 6px;
    font-size: 13px; letter-spacing: 9px;
  }
  .front-strip {
    position: absolute; left: 0; right: 0; top: 164px; height: 38px;
    background: var(--strip-grey);
    display: flex; align-items: center; padding-left: 36px;
    color: var(--brand-blue);
  }
  .holder-name { font-weight: 700; font-size: 19px; }
  .holder-role { font-size: 14px; margin-left: 10px; padding-left: 10px; border-left: 1px solid var(--brand-blue); }
  .front-band {
    position: absolute; left: 0; right: 0; top: 202px; bottom: 0;
    background: var(--brand-blue);
    color: var(--ink-white);
    padding: 12px 36px 0;
    font-size: 13.5px; line-height: 17px; font-weight: 500;
  }
  .contact-gap { height: 6px; }
  .contact-label { font-weight: 700; }

  /* Back */
  .card-back { background: var(--brand-blue); color: var(--ink-white); }
  .back-brand {
    position: absolute; left: 40px; top: 34px;
    display: flex; align-items: center; gap: 16px;
  }
  .back-brand .brand-square { background: var(--ink-white); }
  .back-brand .brand-divider { background: var(--ink-white); }
  .back-brand .brand-name { color: var(--ink-white); }
  .service-list {
    position: absolute; left: 40px; top: 122px;
    list-style: none;
    font-size: 14px; font-weight: 500; line-height: 24px;
  }
  .service-list li { display: flex; align-items: center; gap: 10px; }
  .service-bullet { width: 9px; height: 9px; background: var(--ink-white); flex: none; }
  .back-strip {
    position: absolute; left: 0; right: 0; bottom: 0; height: 30px;
    background: var(--card-white);
    display: flex; align-items: center; padding-left: 40px;
    color: var(--brand-blue); font-size: 13px; font-weight: 700; letter-spacing: .5px;
  }
</style>
</head>
<body>
<main class="stage">

  <section class="card card-front" aria-label="Business card front">
    <div class="front-brand">
      <span class="brand-square"></span>
      <span class="brand-divider"></span>
      <span class="brand-name">BUILDMARQ<span class="brand-sub">SOLUTIONS</span></span>
    </div>
    <div class="front-strip">
      <span class="holder-name">Dana R. Whitfield</span>
      <span class="holder-role">Owner</span>
    </div>
    <div class="front-band">
      <p>14B Harbor Lane - PMB 118</p>
      <p>Millbrook NY 10560</p>
      <div class="contact-gap"></div>
      <p><span class="contact-label">O:</span> 555-014-2280 ext.100</p>
      <p><span class="contact-label">C:</span> 555-019-4471</p>
      <p><span class="contact-label">E:</span> dana.whitfield@buildmarq-solutions.example</p>
    </div>
  </section>

  <section class="card card-back" aria-label="Business card back">
    <div class="back-brand">
      <span class="brand-square"></span>
      <span class="brand-divider"></span>
      <span class="brand-name">BUILDMARQ<span class="brand-sub">SOLUTIONS</span></span>
    </div>
    <ul class="service-list">
      <li><span class="service-bullet"></span>New Software Implementations</li>
      <li><span class="service-bullet"></span>Software Re-Implementations</li>
      <li><span class="service-bullet"></span>Redesigning Software Usage at the User Level</li>
      <li><span class="service-bullet"></span>Project Coordination &amp; Management</li>
      <li><span class="service-bullet"></span>Continued Software Support</li>
    </ul>
    <div class="back-strip">www.buildmarq-solutions.example</div>
  </section>

</main>
</body>
</html>
```